Tranquil Pathways Hypnotherapy Business Card

Logo attached. (will be printing onto thick white/off white textured card)

Double sided business card for two Therapists working at Tranquil Pathways Hypnotherapy.

Require one design, but with different name and mobile numbers on each card.

Target Market(s)

Medical, Health

Industry/Entity Type

Business

Contact Information for Business Card

Need one business card design, but a separate card for each person - Darren Whitfield and Marike de Bruyn.

FRONT OF CARD

Logo

Name (Darren Whitfield on one card, Marike de Bruyn on the other)
Professional Clinical Hypnotherapist

Consulting Rooms (Near Larkmoor Hospital)
284 Bellcrest Avenue
Ashvale VIC 3189

Darren@TranquilPathwaysHypno.com.au OR Marike@TranquilPathwaysHypno.com.au

Mobile: 0427 862 491 (for Darren) OR
Mobile: 0438 574 206 (for Marike)

BACK OF CARD

Logo

Website: www.TranquilPathwaysHypno.com.au

Phone: 1300 748 519

Requirements
Must have
• Text and logo only. No additiional graphics.

```html
<!DOCTYPE html>
<html lang="en">
<head>
<meta charset="utf-8">
<title>Tranquil Pathways Hypnotherapy – Business Card</title>
<link rel="stylesheet" href="https://fonts.googleapis.com/css2?family=Open+Sans:wght@400;600;700&display=swap">
<style>
  :root {
    --navy: #25306b;
    --navy-light: #2f3b82;
    --grey: #6d6e71;
    --grey-light: #9a9b9e;
    --ink: #2b2b2b;
    --paper: #ffffff;
    --stage: #ecebe8;
  }
  * { margin: 0; padding: 0; box-sizing: border-box; }
  html, body {
    width: 1200px; height: 900px; overflow: hidden;
    background: var(--stage);
    font-family: "Open Sans", Arial, sans-serif;
  }
  .sheet {
    width: 1200px; height: 900px;
    display: flex; align-items: center; justify-content: center; gap: 40px;
  }
  .card {
    position: relative;
    width: 560px; height: 342px;
    overflow: hidden;
    box-shadow: 0 6px 18px rgba(0,0,0,0.18);
  }

  /* Back of card */
  .card--back {
    background: linear-gradient(135deg, var(--navy-light) 0%, var(--navy) 60%);
  }
  .card--back .brand {
    position: absolute; left: 90px; top: 120px;
  }
  .card--back .brand-mark { border-color: var(--grey-light); background: var(--navy); }
  .card--back .brand-name { color: var(--paper); font-size: 22px; }
  .email-tab {
    position: absolute; right: 0; bottom: 0;
    width: 330px; height: 44px;
    background: var(--paper);
    border-top-left-radius: 14px;
    display: flex; align-items: center; justify-content: center;
    color: var(--navy); font-size: 13px; font-weight: 600;
  }

  /* Shared brand lockup */
  .brand { display: flex; align-items: center; gap: 12px; }
  .brand-mark {
    flex: none; width: 56px; height: 56px; border-radius: 50%;
    border: 5px solid var(--grey);
    background: var(--navy);
  }
  .brand-name {
    font-weight: 700; line-height: 1.1; text-transform: uppercase;
    letter-spacing: 0.5px; white-space: nowrap;
  }

  /* Front of card */
  .card--front { background: var(--paper); }
  .holder { position: absolute; left: 32px; top: 26px; }
  .holder-name { color: var(--navy); font-size: 19px; font-weight: 700; }
  .holder-title { color: var(--ink); font-size: 12px; margin-top: 2px; }
  .card--front .brand { position: absolute; left: 300px; top: 44px; gap: 10px; }
  .card--front .brand-mark { width: 44px; height: 44px; border-width: 4px; }
  .card--front .brand-name { color: var(--navy); font-size: 15px; }
  .address {
    position: absolute; left: 32px; top: 128px;
    font-style: normal; color: var(--ink); font-size: 13.5px; line-height: 1.35;
  }
  .contacts {
    position: absolute; left: 32px; top: 200px; list-style: none;
    color: var(--ink); font-size: 14px; line-height: 1.6;
  }
  .contacts li { display: flex; align-items: center; gap: 8px; }
  .contacts svg { width: 13px; height: 13px; fill: var(--navy); }
  .contacts .at { color: var(--navy); font-weight: 700; width: 13px; text-align: center; }
  .footer-band { position: absolute; left: 0; top: 0; width: 560px; height: 342px; }
</style>
</head>
<body>
<main class="sheet">

  <section class="card card--back" aria-label="Back of card">
    <div class="brand">
      <span class="brand-mark"></span>
      <span class="brand-name">Tranquil Pathways<br>Hypnotherapy</span>
    </div>
    <div class="email-tab">Darren@TranquilPathwaysHypno.com.au</div>
  </section>

  <section class="card card--front" aria-label="Front of card">
    <svg class="footer-band" viewBox="0 0 560 342" aria-hidden="true">
      <polygon points="0,258 392,258 402,268 0,268" fill="#9a9b9e"/>
      <polygon points="0,268 402,268 476,342 0,342" fill="#25306b"/>
      <polygon points="452,300 560,300 560,342 494,342" fill="#6d6e71"/>
    </svg>

    <div class="holder">
      <h1 class="holder-name">Darren Whitfield</h1>
      <p class="holder-title">Professional Clinical Hypnotherapist</p>
    </div>

    <div class="brand">
      <span class="brand-mark"></span>
      <span class="brand-name">Tranquil Pathways<br>Hypnotherapy</span>
    </div>

    <address class="address">
      Consulting Rooms (Near Larkmoor Hospital)<br>
      284 Bellcrest Avenue<br>
      Ashvale VIC 3189
    </address>

    <ul class="contacts">
      <li>
        <svg viewBox="0 0 24 24" aria-hidden="true"><path d="M6.6 10.8a15.1 15.1 0 0 0 6.6 6.6l2.2-2.2a1 1 0 0 1 1-.25 11.4 11.4 0 0 0 3.6.57 1 1 0 0 1 1 1V20a1 1 0 0 1-1 1A17 17 0 0 1 3 4a1 1 0 0 1 1-1h3.5a1 1 0 0 1 1 1c0 1.250.2 2.45.57 3.57a1 1 0 0 1-.25 1z"/></svg>
        <span>0427 862 491</span>
      </li>
      <li><span class="at">@</span><span>Darren@TranquilPathwaysHypno.com.au</span></li>
    </ul>
  </section>

</main>
</body>
</html>
```